Baby prediction and advice cards, thank you notes, Baby shower invitations and diaper raffle tickets

Please see attached brief with description of the project.

*** Only apply if you are DETAIL ORIENTED and willing to read 100% the brief and the correction instructions (if required)***

*** Only apply if you are able to communicate in English 100%***

We need QUALITY over quantity

Contact us if you have questions.

Thank you

Target Market(s)

Expecting mothers and their families (Mothers, sisters)

Font styles to use
Sans Serif

Colors

Designer to choose colors to be used in the design.

Requirements
Must have
• Read the brief
Should not have
• Read the brief

```html
<!DOCTYPE html>
<html lang="en">
<head>
<meta charset="utf-8">
<title>Baby Shower Stationery Set</title>
<link rel="stylesheet" href="https://fonts.googleapis.com/css2?family=Amatic+SC:wght@400;700&display=swap">
<style>
  :root{
    --bg:#eceeef;
    --kraft:#c9b797;
    --kraft-edge:#bfad8c;
    --gold:#f1de7a;
    --ink:#ffffff;
    --star-yellow:#f6e36a;
    --star-grey:#b3a68f;
    --font:"Amatic SC", sans-serif;
  }
  *{box-sizing:border-box;margin:0;padding:0}
  html,body{width:1200px;height:1200px;overflow:hidden}
  body{background:var(--bg);position:relative;font-family:var(--font);color:var(--ink)}

  .card{position:absolute;background:var(--kraft);box-shadow:0 2px 6px rgba(0,0,0,.18)}
  .card::before{content:"";position:absolute;inset:7px;border:2px solid var(--gold);pointer-events:none}
  .card .frame{position:absolute;inset:15px;border:2px dashed var(--ink);opacity:.9;pointer-events:none}
  .content{position:absolute;inset:24px}

  .star{position:absolute;width:16px;height:16px;border-radius:4px;background:var(--star-yellow)}
  .star.lg{width:24px;height:24px;border-radius:6px}
  .star.grey{background:var(--star-grey)}

  .line{display:inline-block;border-bottom:1.5px solid var(--ink);height:1.05em;vertical-align:baseline}
  .box{display:inline-block;width:24px;height:20px;border:1.5px solid var(--ink);vertical-align:middle;margin-left:6px}

  /* Prediction & advice card */
  .prediction{left:60px;top:120px;width:550px;height:370px}
  .prediction .title{text-align:center;font-size:46px;font-weight:700;letter-spacing:4px;line-height:1;margin-top:2px}
  .prediction .subtitle{text-align:center;font-size:22px;line-height:1;margin-bottom:14px}
  .prediction .fields{display:grid;grid-template-columns:1fr 1fr;column-gap:24px;font-size:19px;font-weight:700;padding:0 14px}
  .prediction .row{margin-bottom:8px;white-space:nowrap}
  .prediction .stack{display:grid;grid-template-columns:auto auto auto;column-gap:10px;align-items:center;row-gap:4px}

  /* Folded thank-you card */
  .thanks-back{left:660px;top:90px;width:470px;height:300px}
  .thanks-front{left:660px;top:390px;width:470px;height:300px}
  .thanks-front .word{position:absolute;left:0;right:0;top:118px;text-align:center;font-size:48px;font-weight:700;letter-spacing:3px}

  /* Invitation */
  .invite{left:80px;top:560px;width:370px;height:520px}
  .invite .heading{text-align:center;font-weight:700;line-height:.95;margin-top:36px}
  .invite .heading .small{font-size:30px;letter-spacing:2px;display:block}
  .invite .heading .big{font-size:56px;letter-spacing:3px;display:block}
  .invite .lead{font-size:22px;font-weight:700;text-align:center;margin:10px 0 22px}
  .invite .fill{font-size:22px;font-weight:700;padding:0 20px}
  .invite .fill div{margin-bottom:10px;white-space:nowrap}
  .invite .fill .gap{height:26px}

  /* Diaper raffle ticket */
  .raffle{left:480px;top:790px;width:260px;height:150px}
  .raffle .content{inset:24px 24px}
  .raffle .name{font-size:22px;font-weight:700;text-align:center;border-bottom:1.5px solid var(--ink);padding-bottom:2px;margin-top:4px}
  .raffle p{font-size:17px;font-weight:700;text-align:center;line-height:1.05;margin:6px 0}
  .raffle .who{font-size:18px;font-weight:700}

  /* Inside message card */
  .message{left:780px;top:740px;width:390px;height:280px}
  .message .rule{position:absolute;left:135px;right:135px;top:88px;border-top:2px solid var(--ink)}
  .message p{position:absolute;left:40px;right:40px;top:100px;text-align:center;font-size:24px;font-weight:700;letter-spacing:1px;line-height:1.05}
</style>
</head>
<body>

<section class="card prediction">
  <div class="frame"></div>
  <span class="star lg" style="left:28px;top:26px" role="img" aria-label="hand-drawn star doodle"></span>
  <span class="star grey" style="left:54px;top:40px" role="img" aria-label="hand-drawn star doodle"></span>
  <span class="star grey" style="right:30px;top:34px" role="img" aria-label="hand-drawn star doodle"></span>
  <span class="star grey lg" style="right:50px;top:64px" role="img" aria-label="hand-drawn star doodle"></span>
  <span class="star grey" style="left:250px;top:176px" role="img" aria-label="hand-drawn star doodle"></span>
  <span class="star grey" style="left:60px;top:250px" role="img" aria-label="hand-drawn star doodle"></span>
  <div class="content">
    <h1 class="title">Baby</h1>
    <p class="subtitle">prediction and advice</p>
    <div class="fields">
      <div>
        <div class="row">Baby's name: <span class="line" style="width:120px"></span></div>
        <div class="row stack">
          <span>Gender: Boy</span><span class="box"></span><span>Weight:</span>
          <span style="text-align:right">Girl</span><span class="box"></span><span>Length:</span>
        </div>
        <div class="row stack" style="margin-top:22px">
          <span>Resemblance: All dad</span><span class="box"></span><span></span>
          <span style="text-align:right">All mom</span><span class="box"></span><span></span>
          <span style="text-align:right">Both</span><span class="box"></span><span></span>
        </div>
        <div class="row" style="margin-top:8px">My best advice: <span class="line" style="width:110px"></span></div>
        <div class="row"><span class="line" style="width:220px"></span></div>
      </div>
      <div>
        <div class="row">Date of birth: <span class="line" style="width:110px"></span></div>
        <div class="row">Time of birth: <span class="line" style="width:110px"></span></div>
        <div class="row">Hair color: <span class="line" style="width:120px"></span></div>
        <div class="row">Eye color: <span class="line" style="width:125px"></span></div>
        <div class="row" style="margin-top:16px">I hope you get dad's: <span class="line" style="width:80px"></span></div>
        <div class="row">I hope you get mom's: <span class="line" style="width:80px"></span></div>
        <div class="row" style="margin-top:22px">Best wishes and love from: <span class="line" style="width:60px"></span></div>
        <div class="row"><span class="line" style="width:220px"></span></div>
      </div>
    </div>
  </div>
</section>

<section class="card thanks-back">
  <div class="frame"></div>
  <span class="star" style="left:228px;top:102px" role="img" aria-label="hand-drawn star doodle"></span>
</section>

<section class="card thanks-front">
  <div class="frame"></div>
  <span class="star lg" style="left:26px;top:26px" role="img" aria-label="hand-drawn star doodle"></span>
  <span class="star grey" style="left:52px;top:44px" role="img" aria-label="hand-drawn star doodle"></span>
  <span class="star grey" style="left:34px;top:64px" role="img" aria-label="hand-drawn star doodle"></span>
  <span class="star grey" style="right:30px;top:40px" role="img" aria-label="hand-drawn star doodle"></span>
  <span class="star grey" style="left:40px;bottom:40px" role="img" aria-label="hand-drawn star doodle"></span>
  <span class="star" style="right:46px;bottom:50px" role="img" aria-label="hand-drawn star doodle"></span>
  <span class="star grey" style="right:70px;bottom:30px" role="img" aria-label="hand-drawn star doodle"></span>
  <p class="word">"Thank you"</p>
</section>

<section class="card invite">
  <div class="frame"></div>
  <span class="star lg" style="left:30px;top:30px" role="img" aria-label="hand-drawn star doodle"></span>
  <span class="star grey" style="left:58px;top:52px" role="img" aria-label="hand-drawn star doodle"></span>
  <span class="star grey" style="left:36px;top:74px" role="img" aria-label="hand-drawn star doodle"></span>
  <span class="star grey lg" style="right:44px;top:30px" role="img" aria-label="hand-drawn star doodle"></span>
  <span class="star grey" style="right:42px;bottom:84px" role="img" aria-label="hand-drawn star doodle"></span>
  <span class="star lg" style="right:30px;bottom:52px" role="img" aria-label="hand-drawn star doodle"></span>
  <div class="content">
    <h2 class="heading">
      <span class="small">Celebrating</span>
      <span class="big">A Baby</span>
      <span class="small">On the way</span>
    </h2>
    <p class="lead">"Join us for a shower honoring: <span class="line" style="width:40px"></span></p>
    <div class="fill">
      <div><span class="line" style="width:260px"></span></div>
      <div>Time: <span class="line" style="width:200px"></span></div>
      <div>Place: <span class="line" style="width:196px"></span></div>
      <div>Details: <span class="line" style="width:180px"></span></div>
      <div class="gap"></div>
      <div>RSVP to: <span class="line" style="width:176px"></span></div>
      <div>Hosted by: <span class="line" style="width:164px"></span></div>
    </div>
  </div>
</section>

<section class="card raffle">
  <div class="frame"></div>
  <span class="star" style="left:24px;top:22px" role="img" aria-label="hand-drawn star doodle"></span>
  <span class="star grey" style="right:26px;bottom:24px" role="img" aria-label="hand-drawn star doodle"></span>
  <div class="content">
    <div class="name">Diaper raffle ticket</div>
    <p>Bring a pack of diapers (any size)<br>for your chance to win a prize!</p>
    <div class="who">Name: <span class="line" style="width:150px"></span></div>
  </div>
</section>

<section class="card message">
  <div class="frame"></div>
  <span class="star lg" style="left:26px;top:56px" role="img" aria-label="hand-drawn star doodle"></span>
  <span class="star grey" style="left:52px;top:70px" role="img" aria-label="hand-drawn star doodle"></span>
  <span class="star grey" style="right:30px;top:28px" role="img" aria-label="hand-drawn star doodle"></span>
  <span class="star" style="left:188px;top:70px;width:12px;height:12px" role="img" aria-label="hand-drawn star doodle"></span>
  <span class="star lg" style="right:32px;bottom:70px" role="img" aria-label="hand-drawn star doodle"></span>
  <span class="star grey" style="right:50px;bottom:44px" role="img" aria-label="hand-drawn star doodle"></span>
  <span class="star grey" style="left:100px;bottom:28px" role="img" aria-label="hand-drawn star doodle"></span>
  <div class="rule"></div>
  <p>"For being with me and sharing in<br>the celebration of this<br>wonderful occasion."</p>
</section>

</body>
</html>
```